Business Card Design using new logo

As much as we'd like to think that treating everyone equally is the best strategy for fairness, the reality is that the differences in the lives of women and men have to be taken into account to ensure that organizations, programs, services, and yes, even public policy treat women and men in ways that achieve gender equity.

That's where ParityLoom - balance insight metrics comes in. Using the data-driven tools of gender analysis, our organization can help anyone determine if gender equity is being achieved - in businesses and organizations, in the planning and implementation of programs and services, and in the development and enforcement of public policy.
Updates

Apologies for the delay - have not had time to finalize the decision.  Should be early this week - probably Tuesday.

Industry/Entity Type

Business

Requirements
Must have
• New Logo for ParityLoom
• Logo plus words "Balance Insight Metrics"

```html
<!DOCTYPE html>
<html lang="en">
<head>
<meta charset="utf-8">
<title>ParityLoom Business Card</title>
<link rel="stylesheet" href="https://fonts.googleapis.com/css2?family=Mulish:wght@400;700&display=swap">
<style>
  :root {
    --backdrop: #8d8b86;
    --card-dark: #1e1e1e;
    --card-light: #fbfbfb;
    --ink: #1f1f1f;
    --ink-soft: #3a3a3a;
    --logo-grey: #b9b9b9;
    --accent: #f0901e;
    --social: #3aa3dc;
  }
  * { margin: 0; padding: 0; box-sizing: border-box; }
  html, body { width: 1200px; height: 871px; overflow: hidden; }
  body {
    background: var(--backdrop);
    font-family: "Mulish", sans-serif;
    position: relative;
  }
  .card {
    position: absolute;
    width: 600px;
    height: 343px;
    border-radius: 3px;
    box-shadow: 0 10px 30px rgba(0,0,0,0.35);
  }
  .card-front {
    left: 90px; top: 90px;
    background: var(--card-dark);
  }
  .card-front .lockup {
    position: absolute;
    left: 0; right: 0; top: 128px;
    text-align: center;
  }
  .card-front .brand-name {
    font-size: 58px;
    line-height: 64px;
    font-weight: 400;
    color: var(--logo-grey);
    letter-spacing: 0.5px;
  }
  .card-front .tagline {
    margin-top: 6px;
    font-size: 15px;
    letter-spacing: 3px;
    text-transform: uppercase;
    color: var(--accent);
  }
  .card-back {
    left: 510px; top: 438px;
    background: var(--card-light);
  }
  .card-back .lockup {
    position: absolute;
    left: 40px; top: 118px;
  }
  .card-back .brand-name {
    font-size: 42px;
    line-height: 48px;
    font-weight: 400;
    color: var(--ink);
  }
  .card-back .tagline {
    margin-top: 4px;
    font-size: 11px;
    letter-spacing: 2px;
    text-transform: uppercase;
    color: var(--accent);
  }
  .social {
    position: absolute;
    left: 28px; bottom: 26px;
    display: flex; align-items: center; gap: 10px;
    font-size: 13px; color: var(--ink-soft);
  }
  .social-mark {
    width: 12px; height: 12px;
    background: var(--social);
    border-radius: 2px;
  }
  .contact {
    position: absolute;
    left: 362px; top: 58px;
    color: var(--ink-soft);
  }
  .contact .person { font-size: 19px; font-weight: 700; color: var(--ink); }
  .contact .role { font-size: 15px; color: var(--accent); margin-bottom: 14px; }
  .contact .company { font-size: 14px; font-weight: 700; color: var(--accent); }
  .contact .address { font-size: 14px; line-height: 19px; margin-bottom: 8px; }
  .contact-list { list-style: none; }
  .contact-list li {
    display: flex; align-items: center; gap: 14px;
    font-size: 14px; line-height: 22px;
  }
  .contact-list svg { width: 11px; height: 11px; fill: var(--accent); }
  .contact-list .icon-mail { fill: none; stroke: var(--accent); stroke-width: 1.6; }
</style>
</head>
<body>
  <section class="card card-front">
    <div class="lockup">
      <div class="brand-name">ParityLoom</div>
      <div class="tagline">Balance Insight Metrics</div>
    </div>
  </section>

  <section class="card card-back">
    <div class="lockup">
      <div class="brand-name">ParityLoom</div>
      <div class="tagline">Balance Insight Metrics</div>
    </div>

    <div class="social">
      <span>@Parity_Loom</span>
      <span class="social-mark"></span>
    </div>

    <div class="contact">
      <div class="person">Mara Ellison</div>
      <div class="role">Ceo</div>
      <div class="company">ParityLoom.inc</div>
      <div class="address">P O Box 402<br>Westhaven 6120</div>
      <ul class="contact-list">
        <li><svg viewBox="0 0 12 12"><path d="M2 1h3l1 3-2 1a7 7 0 0 0 3 3l1-2 3 1v3c-6 0-10-4-10-9z"/></svg>0800 555 310</li>
        <li><svg viewBox="0 0 12 12"><rect x="3" y="0" width="6" height="12" rx="1"/></svg>+64 21 555 482</li>
        <li><svg viewBox="0 0 12 12"><path class="icon-mail" d="M1 2.5h10v7H1z M1 2.5l5 4 5-4"/></svg>mara@parityloom.com</li>
        <li><svg viewBox="0 0 12 12"><circle cx="6" cy="6" r="6"/></svg>parityloom.com</li>
      </ul>
    </div>
  </section>
</body>
</html>
```